Business card design needed

Need a new business card design for a new business in Sydney, Australia called 'Tarrow Australia'. The business deals in consulting for new sales, sales leadership and customer service consultancy. Want the business card to look professional and clean

Industry/Entity Type

Leadership

Contact Information for Business Card

Tarrow Australia
Peter Holm
Managing Director

14 Corvane Street
Brackmere NSW 2095

0455 913 702
peter@tarrow.com.au
www.tarrow.com.au

```html
<!DOCTYPE html>
<html lang="en">
<head>
<meta charset="utf-8">
<title>Tarrow Australia – Business Card</title>
<link rel="stylesheet" href="https://fonts.googleapis.com/css2?family=Arimo:wght@400;700&display=swap">
<style>
  :root {
    --card-bg: #ffffff;
    --ink: #111111;
    --accent-red: #e8220f;
    --accent-blue: #0a1eb4;
    --font-main: "Arimo", Arial, Helvetica, sans-serif;
  }
  html, body {
    margin: 0;
    padding: 0;
    overflow: hidden;
    background: var(--card-bg);
  }
  .card {
    position: relative;
    width: 1200px;
    height: 741px;
    overflow: hidden;
    background: var(--card-bg);
    font-family: var(--font-main);
    color: var(--ink);
  }
  .card__web {
    position: absolute;
    left: 22px;
    top: 38px;
    margin: 0;
    font-size: 22px;
    letter-spacing: 0.5px;
  }
  .card__person {
    position: absolute;
    right: 40px;
    top: 32px;
    margin: 0;
    text-align: right;
  }
  .card__name {
    display: block;
    font-size: 28px;
    letter-spacing: 4.5px;
    line-height: 36px;
  }
  .card__role {
    display: block;
    font-size: 28px;
    letter-spacing: 4.5px;
    line-height: 36px;
    color: var(--accent-red);
  }
  .brand {
    position: absolute;
    left: 0;
    right: 0;
    top: 300px;
    display: flex;
    align-items: center;
    justify-content: center;
    gap: 22px;
  }
  .brand__mark {
    width: 34px;
    height: 34px;
    background: var(--accent-red);
  }
  .brand__name {
    margin: 0;
    font-size: 72px;
    font-weight: 700;
    letter-spacing: -1px;
    color: var(--ink);
    line-height: 1;
  }
  .card__contact {
    position: absolute;
    left: 0;
    right: 0;
    top: 666px;
    margin: 0;
    text-align: center;
    font-size: 23px;
    letter-spacing: 0.3px;
  }
</style>
</head>
<body>
  <main class="card">
    <p class="card__web">www.tarrow.com.au</p>

    <p class="card__person">
      <span class="card__name">Peter Holm</span>
      <span class="card__role">Managing Director</span>
    </p>

    <div class="brand">
      <span class="brand__mark" aria-hidden="true"></span>
      <h1 class="brand__name">Tarrow Australia</h1>
    </div>

    <p class="card__contact">14 Corvane Street Brackmere NSW 2095 0455 913 702 peter@tarrow.com.au</p>
  </main>
</body>
</html>
```